Business Card & Email Signature Design || Upmarket + Luxury

Rima Vale Honey, a New Zealand Manuka Honey company needs a Business Card & Email Signature design.

Our logo's are attached in Gold & Black versions, feel free to be creative with how you use the logo and it's patterns in your design.

Style:
- Looking for an Elegant, Luxurious, Upmarket feel.
- Black/Matte Black Card, Gold Foil, UV Embossing

Information to Add:

- Logo
- Company Name: Rima Vale Honey
- Name: Martin Delrow
- Title: Creative Director
- Phone: +64 2815 90 617
- Email: martin@rimavalehoney.example.nz
- Website: www.rimavalehoney.example.nz

- Socials: ***For email Signature Only***
- Facebook: https://www.facebook.com/rimavalehoney/
- Instagram: https://www.instagram.com/rimavalehoney/

Target Market(s)

Asia/Europe Luxury, Upmarket

Contact Information for Business Card

- Logo
- Name: Martin Delrow
- Phone: +64 2815 90 617

Font styles to use
Other font styles liked:
• Champagne & Limousines (Attached)

Requirements
Must have
• Business Card & Email Signature Design.

Looking for a Sleek, Luxury, Upmarket Design.

```html
<!DOCTYPE html>
<html lang="en">
<head>
<meta charset="utf-8">
<title>Rima Vale Honey — Business Card &amp; Email Signature</title>
<link rel="stylesheet" href="https://fonts.googleapis.com/css2?family=Quicksand:wght@400;500;600&display=swap">
<style>
  :root {
    --page: #ffffff;
    --card: #030303;
    --gold: #dcbc6e;
    --gold-soft: #c9a85c;
    --comb: rgba(190, 155, 80, 0.34);
    --comb-fade: rgba(190, 155, 80, 0);
  }
  * { box-sizing: border-box; margin: 0; padding: 0; }
  html, body { width: 1200px; height: 1000px; overflow: hidden; background: var(--page); }
  body { position: relative; font-family: "Quicksand", sans-serif; color: var(--gold); }

  .card {
    position: absolute;
    background: var(--card);
    overflow: hidden;
    box-shadow: 4px 10px 14px rgba(0, 0, 0, 0.45);
  }
  .card--front { left: 82px; top: 232px; width: 489px; height: 278px; }
  .card--back  { left: 621px; top: 232px; width: 486px; height: 276px; }
  .signature   { left: 323px; top: 692px; width: 600px; height: 201px; box-shadow: none; }

  .honeycomb { position: absolute; left: 0; right: 0; }
  .honeycomb--top    { top: 0;    background: linear-gradient(to bottom, var(--comb), var(--comb-fade)); }
  .honeycomb--bottom { bottom: 0; background: linear-gradient(to top, var(--comb), var(--comb-fade)); }

  .card--front .honeycomb--top    { height: 105px; }
  .card--front .honeycomb--bottom { height: 95px; }
  .card--back .honeycomb--top     { height: 50px; }
  .card--back .honeycomb--bottom  { height: 44px; }
  .signature .honeycomb--top      { height: 68px; }

  .brand-mark {
    position: absolute;
    border-radius: 50%;
    border: 1.5px solid var(--gold);
  }
  .card--front .brand-mark { left: 64px; top: 106px; width: 66px; height: 66px; }
  .card--back .brand-mark  { left: 231px; top: 26px; width: 24px; height: 24px; }
  .signature .brand-mark   { left: 108px; top: 24px; width: 44px; height: 44px; }

  .brand-name {
    position: absolute;
    font-weight: 500;
    color: var(--gold);
    letter-spacing: 0.12em;
    text-transform: uppercase;
    white-space: nowrap;
  }
  .card--front .brand-name { left: 160px; top: 124px; font-size: 24px; }
  .card--back .brand-name  { left: 0; right: 0; top: 62px; text-align: center; font-size: 12px; }
  .signature .brand-name   { left: 20px; width: 220px; top: 98px; text-align: center; font-size: 17px; }

  .person-name { position: absolute; font-weight: 600; color: var(--gold); white-space: nowrap; }
  .person-title { position: absolute; font-weight: 400; color: var(--gold-soft); white-space: nowrap; }
  .card--back .person-name  { left: 0; right: 0; top: 100px; text-align: center; font-size: 23px; }
  .card--back .person-title { left: 0; right: 0; top: 130px; text-align: center; font-size: 13px; }

  .contact { position: absolute; display: flex; align-items: center; gap: 6px; white-space: nowrap; font-weight: 400; color: var(--gold); }
  .contact svg { flex: none; }
  .card--back .contact { left: 0; right: 0; justify-content: center; font-size: 13.5px; }
  .card--back .contact--phone { top: 169px; }
  .card--back .contact--email { top: 191px; }
  .card--back .website { position: absolute; left: 0; right: 0; top: 242px; text-align: center; font-size: 12px; }

  .signature .website { position: absolute; left: 20px; width: 220px; top: 146px; text-align: center; font-size: 11px; font-weight: 500; }
  .signature .person-name  { left: 266px; top: 90px; font-size: 20px; }
  .signature .person-title { left: 266px; top: 118px; font-size: 13px; color: var(--gold); }
  .signature .contact { font-size: 12.5px; }
  .signature .contact--phone { left: 410px; top: 96px; }
  .signature .contact--email { left: 410px; top: 116px; font-size: 10.5px; gap: 5px; }
  .signature .contact--facebook { left: 266px; top: 149px; }
  .signature .contact--instagram { left: 410px; top: 149px; }
  .dot { width: 16px; height: 16px; border-radius: 50%; background: var(--gold); }
</style>
</head>
<body>

  <section class="card card--front" aria-label="Business card front">
    <div class="honeycomb honeycomb--top" role="img" aria-label="Gold honeycomb hexagon pattern"></div>
    <div class="honeycomb honeycomb--bottom" role="img" aria-label="Gold honeycomb hexagon pattern"></div>
    <span class="brand-mark" aria-hidden="true"></span>
    <p class="brand-name">Rima Vale Honey</p>
  </section>

  <section class="card card--back" aria-label="Business card back">
    <div class="honeycomb honeycomb--top" role="img" aria-label="Gold honeycomb hexagon pattern"></div>
    <div class="honeycomb honeycomb--bottom" role="img" aria-label="Gold honeycomb hexagon pattern"></div>
    <span class="brand-mark" aria-hidden="true"></span>
    <p class="brand-name">Rima Vale Honey</p>
    <p class="person-name">Martin Delrow</p>
    <p class="person-title">Creative Director</p>
    <p class="contact contact--phone">
      <svg width="10" height="15" viewBox="0 0 10 15" aria-hidden="true"><rect x="1" y="0.75" width="8" height="13.5" rx="1.5" fill="none" stroke="currentColor" stroke-width="1.5"/><circle cx="5" cy="11.5" r="0.9" fill="currentColor"/></svg>
      +64 2815 90 617
    </p>
    <p class="contact contact--email">
      <svg width="12" height="9" viewBox="0 0 12 9" aria-hidden="true"><rect x="0.5" y="0.5" width="11" height="8" fill="none" stroke="currentColor"/><path d="M0.5 0.5 L6 5 L11.5 0.5" fill="none" stroke="currentColor"/></svg>
      martin@rimavalehoney.example.nz
    </p>
    <p class="website">www.rimavalehoney.example.nz</p>
  </section>

  <section class="card signature" aria-label="Email signature">
    <div class="honeycomb honeycomb--top" role="img" aria-label="Gold honeycomb hexagon pattern"></div>
    <span class="brand-mark" aria-hidden="true"></span>
    <p class="brand-name">Rima Vale Honey</p>
    <p class="website">www.rimavalehoney.example.nz</p>
    <p class="person-name">Martin Delrow</p>
    <p class="person-title">Creative Director</p>
    <p class="contact contact--phone">
      <svg width="9" height="14" viewBox="0 0 10 15" aria-hidden="true"><rect x="1" y="0.75" width="8" height="13.5" rx="1.5" fill="none" stroke="currentColor" stroke-width="1.5"/><circle cx="5" cy="11.5" r="0.9" fill="currentColor"/></svg>
      +64 2815 90 617
    </p>
    <p class="contact contact--email">
      <svg width="11" height="8" viewBox="0 0 12 9" aria-hidden="true"><rect x="0.5" y="0.5" width="11" height="8" fill="none" stroke="currentColor"/><path d="M0.5 0.5 L6 5 L11.5 0.5" fill="none" stroke="currentColor"/></svg>
      martin@rimavalehoney.example.nz
    </p>
    <p class="contact contact--facebook"><span class="dot"></span>rimavalehoney</p>
    <p class="contact contact--instagram"><span class="dot"></span>rimavalehoney</p>
  </section>

</body>
</html>
```